New Alcoholic Spiked Seltzer Line

We need a can design for a line of low calorie alcoholic seltzer. This product is a sparkling water and vodka drink with no sugar added in a slim 12 oz can.

This is a lighter, healthier, alternative to the sugary ready-to-drinks on the market. The product contains only 3 ingredients: Vodka, Water and Natural Flavors. It has only 100 calories but still has 5% alcohol, so you don't need to sacrifice alcohol to cut calories.

This product also does not contain any preservatives.

We want this design to communicate the following objectives to the consumer and in this order:

1. Appetizing product
2.Low calorie
3.Communicate the type of beverage (Spiked Seltzer)

The brand name of the product is VELKA.

The flavor of the product needed to be used for the design is Mango-Orange.

Comparable products are:

www.brisavelfizz.example/
https://www.tarnowbubble.example
https://quellrind.example/

The designs should not infringe or copy the creative directions of the products mentionned above. They are only given so that you can better understand the type of product we are developing.

Target Market(s)

Young Professional women between the ages of 25 and 44

Industry/Entity Type

Product

Colors

Designer to choose colors to be used in the design.

Requirements
Must have
• Design extendibility, meaning it can be adapted for other flavors.
• This is a new category in the market we are targeting, so consumers must easily be able to identify what type of product this is.

```html
<!DOCTYPE html>
<html lang="en">
<head>
<meta charset="utf-8">
<title>VELKA Spiked Seltzer – Mango Orange Can Label</title>
<link rel="stylesheet" href="https://fonts.googleapis.com/css2?family=Josefin+Sans:wght@300;600;700&display=swap">
<style>
  :root {
    --bg-light: #c4702a;
    --bg-deep: #b9521f;
    --label-white: #f6f6f4;
    --ink: #2a2522;
    --accent-red: #e0573a;
    --mango-light: #f1c088;
    --mango-mid: #e98a3b;
    --mango-deep: #c3401e;
    --text-white: #ffffff;
  }
  * { margin: 0; padding: 0; box-sizing: border-box; }
  html, body { width: 1200px; height: 1200px; overflow: hidden; }
  body {
    background: linear-gradient(135deg, var(--bg-light) 0%, var(--bg-deep) 100%);
    font-family: "Josefin Sans", sans-serif;
    position: relative;
  }
  .can-label {
    position: absolute;
    left: 360px;
    top: 100px;
    width: 480px;
    height: 1000px;
    border-radius: 24px;
    background: var(--label-white);
    overflow: hidden;
  }
  .flavour-artwork {
    position: absolute;
    left: 0;
    top: 330px;
    width: 480px;
    height: 670px;
    background: linear-gradient(180deg,
      var(--label-white) 0%,
      var(--mango-light) 30%,
      var(--mango-mid) 60%,
      var(--mango-deep) 100%);
  }
  .brand-name {
    position: absolute;
    top: 62px;
    width: 100%;
    text-align: center;
    font-weight: 700;
    font-size: 112px;
    letter-spacing: 4px;
    color: var(--ink);
    line-height: 1;
  }
  .category {
    position: absolute;
    top: 200px;
    width: 100%;
    text-align: center;
    font-weight: 600;
    font-size: 34px;
    letter-spacing: 2px;
    color: var(--accent-red);
  }
  .calorie-info {
    position: absolute;
    right: 30px;
    top: 440px;
    width: 200px;
    text-align: center;
    color: var(--ink);
  }
  .calorie-info .claim {
    font-weight: 600;
    font-size: 14px;
    letter-spacing: 1.5px;
  }
  .calorie-info .count {
    font-weight: 700;
    font-size: 58px;
    line-height: 1;
    margin-top: 8px;
  }
  .calorie-info .unit {
    font-weight: 600;
    font-size: 16px;
    letter-spacing: 1px;
    margin-bottom: 8px;
  }
  .flavour {
    position: absolute;
    left: 30px;
    top: 660px;
    width: 420px;
    text-align: center;
    font-weight: 700;
    font-size: 60px;
    line-height: 0.95;
    letter-spacing: 2px;
    color: var(--ink);
  }
  .description {
    position: absolute;
    left: 30px;
    top: 800px;
    width: 420px;
    text-align: center;
    font-weight: 300;
    font-size: 31px;
    line-height: 1.1;
    color: var(--text-white);
  }
</style>
</head>
<body>
  <main class="can-label">
    <div class="flavour-artwork" role="img" aria-label="Mango and orange flavour artwork with rising bubbles"></div>

    <h1 class="brand-name">VELKA</h1>
    <p class="category">SPIKED SELZER</p>

    <div class="calorie-info">
      <p class="claim">LOW CALORIE &amp; CARB</p>
      <p class="count">100</p>
      <p class="unit">CALORIES</p>
      <p class="claim">NATURAL FLAVOURINGS</p>
    </div>

    <h2 class="flavour">MANGO<br>ORANGE</h2>
    <p class="description">SPARKLING WATER<br>&amp; VODKA DRINK</p>
  </main>
</body>
</html>
```